Arvo 7 Detection Wheel

We need a professional **framework wheel diagram** designed for our detection dog training manual.

Our business is **Arvo 7 Dog Training**, and this graphic represents our **Detection Training Model**.

Please use the **attached reference images** as a guide for the structure and layout of the wheel.

### What we need

1. **Full wheel graphic**

* Clean circular framework wheel
* Similar structure to the attached example
* Clear sections and text
* Professional training manual style
* Transparent background

2. **Individual segment pieces**

We also need the **inner sections broken into separate pieces** (like the second reference image).

This will allow us to place each section on different pages of the manual when explaining the concepts.

Each piece should look like a **slice of the wheel**.

### Style

The design should look:

• Professional
• Clean and modern
• Structured and easy to read
• Suitable for a training manual

Avoid cartoon styles or clipart.

### Colours

Please use our brand colour palette (see attached image):

* Dark navy blue
* Steel blue
* Light blue
* White
* Light grey
* Dark grey

### Files required

Final files must include:

* Vector files (AI or EPS)
* Transparent PNG
* High-resolution PDF

Please also provide **each segment exported individually**

```html
<!DOCTYPE html>
<html lang="en">
<head>
<meta charset="utf-8">
<title>Arvo 7 Detection Wheel</title>
<link rel="stylesheet" href="https://fonts.googleapis.com/css2?family=Open+Sans:wght@600;700;800&display=swap">
<style>
  :root {
    --navy: #1c2d4f;
    --navy-band: #2a3f66;
    --steel: #3d5784;
    --steel-light: #4b6898;
    --sky-1: #bcd9e8;
    --sky-2: #a1c4dd;
    --sky-3: #c9e6f2;
    --sky-4: #afd2e6;
    --sky-5: #b7d7e9;
    --grey-band: #a9bccf;
    --white: #ffffff;
    --ink: #1a2a48;
  }
  html, body {
    margin: 0;
    padding: 0;
    width: 1200px;
    height: 800px;
    overflow: hidden;
    background: var(--white);
  }
  .wheel {
    display: block;
    width: 1200px;
    height: 800px;
    font-family: "Open Sans", sans-serif;
  }
  .ring-outer { fill: var(--navy); }
  .ring-line { fill: none; stroke: var(--white); stroke-width: 4; }
  .band-outer { fill: var(--navy-band); }
  .divider { stroke: var(--white); stroke-width: 3; opacity: .85; }
  .logo-field { fill: var(--white); }
  .logo-name { fill: var(--navy); font-weight: 800; font-size: 50px; letter-spacing: 1px; }
  .ring-dog { fill: var(--navy); }
  .ring-title { fill: var(--white); font-weight: 600; font-size: 30px; letter-spacing: 3px; }
  .ring-title-dog { fill: var(--white); font-weight: 600; font-size: 25px; letter-spacing: 2px; }
  .ring-title-handler { fill: var(--white); font-weight: 700; font-size: 25px; letter-spacing: 2px; }
  .handler-band { fill: none; stroke: var(--grey-band); stroke-width: 32; opacity: .9; }
  .seg-line { stroke: var(--white); stroke-width: 3; }
  .seg-genetic { fill: var(--sky-1); }
  .seg-health { fill: var(--sky-2); }
  .seg-engage { fill: var(--sky-3); }
  .seg-reward { fill: var(--sky-4); }
  .seg-arousal { fill: var(--sky-5); }
  .seg-safety { fill: var(--steel); }
  .seg-coverage { fill: #2f4a76; }
  .seg-minimal { fill: #2c4570; }
  .seg-read { fill: var(--steel-light); }
  .label-outer { fill: var(--white); font-weight: 600; font-size: 24px; }
  .label-dog { fill: var(--ink); font-weight: 600; font-size: 22px; }
  .label-handler { fill: var(--white); font-weight: 600; font-size: 23px; }
  .label-small { font-size: 15px; }
  .hub { fill: var(--white); stroke: #c7d9e6; stroke-width: 6; }
  .hub-title { fill: var(--ink); font-weight: 700; font-size: 38px; }
</style>
</head>
<body>
<svg class="wheel" viewBox="0 0 1536 1024" xmlns="http://www.w3.org/2000/svg" role="img" aria-label="Arvo 7 Detection Training Model wheel">
  <defs>
    <path id="arc-operational-top" d="M 250 512 A 518 450 0 0 1 1286 512"/>
    <path id="arc-operational-bottom" d="M 226 512 A 542 462 0 0 0 1310 512"/>
    <path id="arc-dog" d="M 458 555 A 310 282 0 0 1 1078 555"/>
    <path id="arc-handler" d="M 453 560 A 315 280 0 0 0 1083 560"/>
  </defs>

  <!-- Operational capability ring -->
  <ellipse class="ring-outer" cx="768" cy="512" rx="546" ry="492"/>
  <ellipse class="ring-line" cx="768" cy="522" rx="518" ry="422"/>
  <text class="ring-title"><textPath href="#arc-operational-top" startOffset="50%" text-anchor="middle">OPERATIONAL CAPABILITY AREA</textPath></text>
  <text class="ring-title"><textPath href="#arc-operational-bottom" startOffset="50%" text-anchor="middle">OPERATIONAL CAPABILITY AREA</textPath></text>

  <!-- Operational segments -->
  <ellipse class="band-outer" cx="768" cy="522" rx="500" ry="410"/>
  <g class="dividers">
    <line class="divider" x1="340" y1="268" x2="500" y2="360"/>
    <line class="divider" x1="280" y1="432" x2="440" y2="470"/>
    <line class="divider" x1="266" y1="558" x2="1272" y2="558"/>
    <line class="divider" x1="375" y1="785" x2="490" y2="705"/>
    <line class="divider" x1="535" y1="895" x2="620" y2="800"/>
    <line class="divider" x1="768" y1="790" x2="768" y2="935"/>
    <line class="divider" x1="1010" y1="898" x2="920" y2="800"/>
    <line class="divider" x1="1175" y1="785" x2="1050" y2="705"/>
    <line class="divider" x1="1258" y1="432" x2="1095" y2="465"/>
    <line class="divider" x1="1195" y1="268" x2="1030" y2="355"/>
  </g>

  <!-- Brand field -->
  <path class="logo-field" d="M 518 171 L 615 258 Q 768 236 918 258 L 1018 171 A 500 410 0 0 0 518 171 Z"/>
  <text class="logo-name" x="768" y="168" text-anchor="middle">Arvo 7</text>

  <!-- Dog foundations ring -->
  <path class="ring-dog" d="M 428 555 A 340 300 0 0 1 1108 555 Z"/>
  <text class="ring-title-dog"><textPath href="#arc-dog" startOffset="50%" text-anchor="middle">DOG FOUNDATIONS</textPath></text>

  <!-- Inner wheel -->
  <g class="inner-wheel" transform="translate(768 555) scale(1 0.88)">
    <path class="seg-genetic" d="M0 0 L-300 0 A300 300 0 0 1 -242.7 -176.3 Z"/>
    <path class="seg-health" d="M0 0 L-242.7 -176.3 A300 300 0 0 1 -92.7 -285.3 Z"/>
    <path class="seg-engage" d="M0 0 L-92.7 -285.3 A300 300 0 0 1 92.7 -285.3 Z"/>
    <path class="seg-reward" d="M0 0 L92.7 -285.3 A300 300 0 0 1 242.7 -176.3 Z"/>
    <path class="seg-arousal" d="M0 0 L242.7 -176.3 A300 300 0 0 1 300 0 Z"/>
    <path class="seg-read" d="M0 0 L300 0 A300 300 0 0 1 212.1 212.1 Z"/>
    <path class="seg-minimal" d="M0 0 L212.1 212.1 A300 300 0 0 1 0 300 Z"/>
    <path class="seg-coverage" d="M0 0 L0 300 A300 300 0 0 1 -212.1 212.1 Z"/>
    <path class="seg-safety" d="M0 0 L-212.1 212.1 A300 300 0 0 1 -300 0 Z"/>
    <g class="seg-lines">
      <line class="seg-line" x1="0" y1="0" x2="-242.7" y2="-176.3"/>
      <line class="seg-line" x1="0" y1="0" x2="-92.7" y2="-285.3"/>
      <line class="seg-line" x1="0" y1="0" x2="92.7" y2="-285.3"/>
      <line class="seg-line" x1="0" y1="0" x2="242.7" y2="-176.3"/>
      <line class="seg-line" x1="0" y1="0" x2="212.1" y2="212.1"/>
      <line class="seg-line" x1="0" y1="0" x2="0" y2="300"/>
      <line class="seg-line" x1="0" y1="0" x2="-212.1" y2="212.1"/>
    </g>
  </g>

  <!-- Handler foundations band -->
  <path class="handler-band" d="M 453 560 A 315 280 0 0 0 1083 560"/>
  <text class="ring-title-handler"><textPath href="#arc-handler" startOffset="56%" text-anchor="middle">HANDLER FOUNDATIONS</textPath></text>

  <!-- Operational labels -->
  <g class="labels-operational" text-anchor="middle">
    <text class="label-outer" x="484" y="248">Development</text>
    <text class="label-outer" x="385" y="385">Integrity</text>
    <text class="label-outer" x="379" y="519">Deployment</text>
    <text class="label-outer" x="385" y="664">Deployment</text>
    <text class="label-outer" x="508" y="806">Reinforcement</text>
    <text class="label-outer" x="670" y="878">Deployment</text>
    <text class="label-outer" x="865" y="870">Search<tspan x="865" dy="28">Method</tspan></text>
    <text class="label-outer" x="1045" y="803">Search<tspan x="1045" dy="28">Method</tspan></text>
    <text class="label-outer" x="1155" y="662">Target<tspan x="1155" dy="28">Odour</tspan></text>
    <text class="label-outer" x="1155" y="513">Target<tspan x="1155" dy="28">Odour</tspan></text>
    <text class="label-outer" x="1135" y="389">Handler</text>
    <text class="label-outer" x="1019" y="248">Distractions</text>
  </g>

  <!-- Dog foundation labels -->
  <g class="labels-dog">
    <text class="label-dog" x="555" y="503" text-anchor="middle">Genetic<tspan x="555" dy="29">Suitability</tspan></text>
    <text class="label-dog" x="567" y="380">Health &amp;<tspan x="567" dy="28">Physical</tspan><tspan x="567" dy="28">Wellbeing</tspan></text>
    <text class="label-dog" x="766" y="331" text-anchor="middle">Engagement<tspan x="766" dy="27">Relationship</tspan></text>
    <text class="label-dog" x="867" y="393">Reward<tspan x="867" dy="28">Value</tspan></text>
    <text class="label-dog" x="928" y="497">Arousal<tspan x="928" dy="28">Regulation</tspan></text>
  </g>

  <!-- Handler foundation labels -->
  <g class="labels-handler">
    <text class="label-handler" x="500" y="609">Dog Safety</text>
    <text class="label-handler" x="636" y="680">Search<tspan x="636" dy="30">Coverage</tspan></text>
    <text class="label-handler" x="794" y="681">Minimal<tspan x="794" dy="29">Necessary</tspan><tspan x="794" dy="27">Involvement</tspan></text>
    <text class="label-handler" x="901" y="611">Read <tspan class="label-small">the</tspan> Dog</text>
  </g>

  <!-- Hub -->
  <ellipse class="hub" cx="768" cy="545" rx="128" ry="90"/>
  <text class="hub-title" x="768" y="512" text-anchor="middle">Detection<tspan x="768" dy="45">Capabilities</tspan></text>
</svg>
</body>
</html>
```